Brenlow Development and Management Corp Stationery Design Project

Based on the logo, a stationary format that can be used for correspondence with all project stakeholders. Typically this involves landowners, public officials, general public, and investors. It needs to be clean and professional, representing the two engineers that manage the company.
Updates

Reason: Logo design finalized. Project updated for revisitation. Thanks,

Target Market(s)

Public officials, investors, project stakeholders, and landowners. All or english speaking, residing in North America. Company is based in Calgary, Alberta, Canada. Project values range fro $10MM to $500MM CAD.

Industry/Entity Type

It Company

Requirements
Should not have
• No references to tropics, palm trees, or similar beaches.

```html
<!DOCTYPE html>
<html lang="en">
<head>
<meta charset="utf-8">
<title>Brenlow Development and Management Corp – Stationery</title>
<link href="https://fonts.googleapis.com/css2?family=Source+Sans+3:wght@400;600;700&display=swap" rel="stylesheet">
<style>
  :root {
    --backdrop: #55585b;
    --slate: #363b42;
    --paper: #f3f3f3;
    --paper-shade: #e9e9ea;
    --lime: #8fae2a;
    --ink: #4a4e54;
    --muted: #a9adb2;
    --rule: #8a8e93;
  }
  * { margin: 0; padding: 0; box-sizing: border-box; }
  html, body { width: 1200px; height: 1000px; overflow: hidden; }
  body {
    background: var(--backdrop);
    font-family: "Source Sans 3", Arial, sans-serif;
    color: var(--ink);
    position: relative;
  }
  .piece { position: absolute; }

  .brand-name {
    font-family: "Source Sans 3", Arial, sans-serif;
    font-weight: 700;
    color: var(--lime);
    letter-spacing: 0.06em;
    line-height: 1;
    display: flex;
    align-items: center;
    gap: 0.35em;
  }
  .brand-mark {
    display: inline-block;
    width: 0.8em; height: 0.8em;
    background: currentColor;
  }
  .brand-tagline {
    font-size: 5.5px;
    color: var(--muted);
    margin-top: 2px;
    letter-spacing: 0.01em;
  }

  /* Presentation folder */
  .folder {
    left: 83px; top: 267px; width: 340px; height: 460px;
    background: var(--slate);
  }
  .folder .brand {
    position: absolute; top: 108px; left: 0; right: 0;
    display: flex; flex-direction: column; align-items: center;
  }
  .folder .brand-name { font-size: 27px; }
  .folder .brand-tagline { font-size: 8.5px; color: var(--muted); margin-top: 4px; }

  /* Letterhead */
  .letterhead {
    left: 453px; top: 282px; width: 312px; height: 441px;
    background: var(--paper);
  }
  .letterhead .brand { position: absolute; left: 27px; top: 27px; }
  .letterhead .brand-name { font-size: 13px; }

  .contact-footer {
    position: absolute;
    border-top: 0.8px solid var(--rule);
    padding-top: 3px;
    font-size: 4.2px;
    line-height: 1.6;
    color: var(--ink);
  }
  .letterhead .contact-footer { left: 15px; width: 185px; bottom: 10px; }

  /* Business cards */
  .card-front {
    left: 811px; top: 283px; width: 107px; height: 55px;
    background: var(--slate);
    display: flex; flex-direction: column; align-items: center; justify-content: center;
  }
  .card-front .brand-name { font-size: 10px; }
  .card-front .brand-tagline { font-size: 3.5px; }

  .card-back {
    left: 990px; top: 256px; width: 126px; height: 81px;
    background: var(--paper);
  }
  .card-back .brand { position: absolute; left: 9px; top: 8px; }
  .card-back .brand-name { font-size: 7px; }
  .card-back .brand-tagline { font-size: 3px; margin-top: 1px; }
  .card-holder { position: absolute; left: 9px; top: 49px; }
  .holder-name { font-size: 6px; color: var(--ink); }
  .holder-role { font-size: 3.4px; color: var(--ink); margin-bottom: 2px; }
  .holder-line { font-size: 3px; line-height: 1.45; color: var(--ink); }

  /* Envelope front */
  .envelope-front {
    left: 798px; top: 362px; width: 329px; height: 165px;
    background: linear-gradient(180deg, var(--paper) 0%, var(--paper-shade) 100%);
  }
  .envelope-front .brand { position: absolute; left: 18px; top: 16px; }
  .envelope-front .brand-name { font-size: 13px; }
  .envelope-front .contact-footer { left: 16px; width: 190px; bottom: 6px; }

  /* Envelope back */
  .envelope-back {
    left: 800px; top: 555px; width: 328px; height: 163px;
    background: var(--paper);
  }
  .envelope-back svg { position: absolute; left: 0; top: 0; }
  .envelope-back .brand {
    position: absolute; left: 0; right: 0; top: 24px;
    display: flex; flex-direction: column; align-items: center;
  }
  .envelope-back .brand-name { font-size: 9px; color: #e6e7e8; }
  .envelope-back .brand-tagline { font-size: 3.2px; color: var(--muted); }
</style>
</head>
<body>

  <section class="piece folder" aria-label="Presentation folder">
    <div class="brand">
      <div class="brand-name"><span class="brand-mark"></span>BRENLOW</div>
      <div class="brand-tagline">Development and Management Corp</div>
    </div>
  </section>

  <section class="piece letterhead" aria-label="Letterhead">
    <div class="brand">
      <div class="brand-name"><span class="brand-mark"></span>BRENLOW</div>
      <div class="brand-tagline">Development and Management Corp</div>
    </div>
    <div class="contact-footer">
      <div>Address: 48 Ridgeview Road, Calgary, AB T2P 0A1 &nbsp;|&nbsp; Phone: +1 555 0142 77</div>
      <div>E-Mail: contact@brenlowdev.ca &nbsp;|&nbsp; Web: www.brenlowdev.ca</div>
    </div>
  </section>

  <section class="piece card-front" aria-label="Business card front">
    <div class="brand-name"><span class="brand-mark"></span>BRENLOW</div>
    <div class="brand-tagline">Development and Management Corp</div>
  </section>

  <section class="piece card-back" aria-label="Business card back">
    <div class="brand">
      <div class="brand-name"><span class="brand-mark"></span>BRENLOW</div>
      <div class="brand-tagline">Development and Management Corp</div>
    </div>
    <div class="card-holder">
      <div class="holder-name">Daniel Marsh</div>
      <div class="holder-role">Managing Partner</div>
      <div class="holder-line">48 Ridgeview Road, Calgary, AB T2P 0A1</div>
      <div class="holder-line">+1 555 0142 77</div>
      <div class="holder-line">contact@brenlowdev.ca</div>
      <div class="holder-line">www.brenlowdev.ca</div>
    </div>
  </section>

  <section class="piece envelope-front" aria-label="Envelope front">
    <div class="brand">
      <div class="brand-name"><span class="brand-mark"></span>BRENLOW</div>
      <div class="brand-tagline">Development and Management Corp</div>
    </div>
    <div class="contact-footer">
      <div>Address: 48 Ridgeview Road, Calgary, AB T2P 0A1 &nbsp;|&nbsp; Phone: +1 555 0142 77</div>
      <div>E-Mail: contact@brenlowdev.ca &nbsp;|&nbsp; Web: www.brenlowdev.ca</div>
    </div>
  </section>

  <section class="piece envelope-back" aria-label="Envelope back">
    <svg width="328" height="163" viewBox="0 0 328 163" aria-hidden="true">
      <path d="M0 0 H328 V44 Q328 60 310 60 H18 Q0 60 0 44 Z" fill="var(--slate)"/>
      <path d="M0 60 L164 64 L328 60" fill="none" stroke="#dcdcdd" stroke-width="0.6"/>
    </svg>
    <div class="brand">
      <div class="brand-name"><span class="brand-mark"></span>BRENLOW</div>
      <div class="brand-tagline">Development and Management Corp</div>
    </div>
  </section>

</body>
</html>
```